Brochure Design Project

I need a brochure design for a full Hair Salon, located in Rockville MD called Coralind Hair, Nails and Spa.
Please use inovative design (the idea is to target an audience between the age of 19 to 50) keeping our main colors (spring green, grey and white).
we would also like to include the list of services which will be provided when needed.

Target Market(s)

women between 19 to 50 - all ethnical backgrounds

Industry/Entity Type

Hair

Requirements
Nice to have
• we would like to include a blurb, contact info and list of prices of all the services we provided. Also we would like to add the line "se habla espaƱol" anywhere in the brochure.

```html
<!DOCTYPE html>
<html lang="en">
<head>
<meta charset="utf-8">
<title>Coralind Hair, Nails and Spa – Services &amp; Price</title>
<link rel="stylesheet" href="https://fonts.googleapis.com/css2?family=Open+Sans:wght@400;600;700;800&display=swap">
<style>
  :root{
    --spring-green:#d0e17c;
    --spring-green-deep:#bdd35f;
    --spring-green-pale:#f1f4e2;
    --slate:#5b5c5e;
    --slate-light:#9a9b9d;
    --paper:#eeeeef;
    --paper-light:#f7f7f7;
    --ink:#262626;
    --white:#ffffff;
  }
  *{margin:0;padding:0;box-sizing:border-box}
  html,body{width:1200px;height:935px;overflow:hidden;background:var(--white)}
  body{font-family:"Open Sans",Arial,sans-serif;color:var(--ink)}
  .brochure-page{position:relative;width:1200px;height:935px;background:var(--white)}
  .page-panel{position:absolute;left:19px;top:18px;width:1160px;height:896px;
    background:linear-gradient(180deg,var(--paper) 0%,var(--paper-light) 70%,var(--paper) 100%)}
  .top-strip{position:absolute;left:19px;top:18px;width:1160px;height:55px;
    background:linear-gradient(90deg,var(--slate-light) 0%,#e4e4e5 30%,#e4e4e5 70%,var(--slate-light) 100%)}
  .title-tab{position:absolute;left:405px;top:18px;width:387px;height:76px;background:var(--slate);
    border-radius:0 0 14px 14px;color:var(--white);font-size:26px;font-weight:400;letter-spacing:.5px;
    display:flex;align-items:center;justify-content:center;padding-top:4px}
  .category-pill{position:absolute;top:108px;width:338px;height:62px;background:var(--spring-green);
    border-radius:16px;display:flex;align-items:center;justify-content:center;
    font-size:25px;font-weight:800;color:var(--ink);letter-spacing:.3px}
  .pill-nails{left:43px}.pill-spa{left:430px}.pill-hair{left:817px}

  .photo-zone{position:absolute}
  .photo-salon{left:19px;top:480px;width:440px;height:384px;
    background:radial-gradient(ellipse at 45% 55%,#c9a878 0%,#b59a74 35%,rgba(200,190,175,.6) 65%,rgba(238,238,239,0) 100%)}
  .photo-hand{left:450px;top:680px;width:470px;height:184px;
    background:radial-gradient(ellipse at 50% 60%,#d9b8a2 0%,#ece2dc 45%,rgba(247,247,247,0) 100%)}
  .photo-lamp{left:880px;top:650px;width:299px;height:214px;
    background:radial-gradient(ellipse at 55% 45%,#ffffff 0%,#f4f4f4 40%,rgba(238,238,239,0) 100%)}

  .price-column{position:absolute;top:186px;font-size:17px;line-height:17.6px}
  .col-nails{left:68px;width:292px}
  .col-spa{left:455px;width:292px}
  .col-hair{left:842px;width:292px}
  .service-group{margin-bottom:17.6px}
  .group-title{font-weight:800;text-transform:uppercase;font-size:16.5px}
  .service-row{display:flex;justify-content:space-between;white-space:nowrap}
  .service-row .price{font-weight:800;width:42px;text-align:left}
  .service-note{white-space:nowrap}

  .language-band{position:absolute;left:19px;top:864px;width:1160px;height:50px;
    background:linear-gradient(90deg,var(--spring-green-deep) 0%,var(--spring-green-pale) 50%,var(--spring-green) 100%);
    display:flex;align-items:center;justify-content:center;font-size:26px;color:var(--ink)}
</style>
</head>
<body>
<div class="brochure-page">
  <div class="page-panel"></div>
  <div class="top-strip"></div>
  <div class="title-tab">SERVICES &amp; PRICE</div>

  <div class="photo-zone photo-salon" role="img" aria-label="Photo of the salon interior with styling chairs and mirrors"></div>
  <div class="photo-zone photo-hand" role="img" aria-label="Photo of a manicured hand resting on a white towel"></div>
  <div class="photo-zone photo-lamp" role="img" aria-label="Photo of a white nail drying lamp"></div>

  <div class="category-pill pill-nails">NAILS</div>
  <div class="category-pill pill-spa">SPA</div>
  <div class="category-pill pill-hair">HAIR</div>

  <section class="price-column col-nails">
    <div class="service-group">
      <div class="group-title">Manicure</div>
      <div class="service-row"><span>Basic manicure</span><span class="price">$15</span></div>
      <div class="service-row"><span>Spa manicure</span><span class="price">$20</span></div>
      <div class="service-row"><span>Hot Oil</span><span class="price">$20</span></div>
      <div class="service-row"><span>French</span><span class="price">$20</span></div>
      <div class="service-row"><span>Gel color manicure</span><span class="price">$30</span></div>
      <div class="service-row"><span>Full set</span><span class="price">$35</span></div>
      <div class="service-note">(classic manicure &amp; pedicure)</div>
      <div class="service-row"><span>Fills</span><span class="price">$25</span></div>
    </div>
    <div class="service-group">
      <div class="group-title">Pedicure</div>
      <div class="service-row"><span>Basic pedicure</span><span class="price">$25</span></div>
      <div class="service-row"><span>Warm lotion</span><span class="price">$35</span></div>
      <div class="service-row"><span>Spa pedicure</span><span class="price">$45</span></div>
      <div class="service-row"><span>Add french</span><span class="price">$5</span></div>
      <div class="service-row"><span>Polish change</span><span class="price">$10</span></div>
      <div class="service-row"><span>Designs</span><span class="price">$3</span></div>
      <div class="service-note">Gel color (add $ 12)</div>
      <div class="service-note">with pedicure</div>
    </div>
  </section>

  <section class="price-column col-spa">
    <div class="service-group">
      <div class="group-title">Facials</div>
      <div class="service-row"><span>European facial</span><span class="price">$85</span></div>
      <div class="service-row"><span>Multi Vitamin facial</span><span class="price">$85</span></div>
      <div class="service-row"><span>Acne facial</span><span class="price">$80</span></div>
      <div class="service-row"><span>Gentleman facial</span><span class="price">$75</span></div>
      <div class="service-row"><span>Lunch break facial</span><span class="price">$45</span></div>
      <div class="service-row"><span>Teen facial</span><span class="price">$50</span></div>
      <div class="service-row"><span>Mini facial</span><span class="price">$45</span></div>
      <div class="service-row"><span>Anti aging facial</span><span class="price">$120</span></div>
      <div class="service-row"><span>Gold facial</span><span class="price">$60</span></div>
      <div class="service-row"><span>Fruit facial</span><span class="price">$45</span></div>
      <div class="service-row"><span>Special bridal facial</span><span class="price">$130</span></div>
    </div>
    <div class="service-group">
      <div class="group-title">Massages</div>
      <div class="service-row"><span>Scalp massages 10 min</span><span class="price">$15</span></div>
      <div class="service-row"><span>Head &amp; neck massage 15 min</span><span class="price">$20</span></div>
      <div class="service-row"><span>Back massage 15 min</span><span class="price">$20</span></div>
      <div class="service-row"><span>Full body massage 60 min</span><span class="price">$75</span></div>
      <div class="service-row"><span>Full body massage 30 min</span><span class="price">$40</span></div>
      <div class="service-row"><span>Foot massage 10 min</span><span class="price">$15</span></div>
      <div class="service-row"><span>Half leg &amp; foot $15 min</span><span class="price">$20</span></div>
    </div>
    <div class="service-group">
      <div class="group-title">Hair Removal</div>
      <div class="service-row"><span>Eyebrow threading</span><span class="price">$12</span></div>
      <div class="service-row"><span>Chin Threading</span><span class="price">$8</span></div>
      <div class="service-row"><span>Upper lip</span><span class="price">$7</span></div>
      <div class="service-row"><span>Lower lip</span><span class="price">$7</span></div>
      <div class="service-row"><span>Forehead</span><span class="price">$10</span></div>
      <div class="service-row"><span>Side burns</span><span class="price">$10</span></div>
      <div class="service-row"><span>Full Face</span><span class="price">$40+</span></div>
    </div>
  </section>

  <section class="price-column col-hair">
    <div class="service-group">
      <div class="group-title">Haircuts</div>
      <div class="service-row"><span>Women’s haircut</span><span class="price">$30</span></div>
      <div class="service-row"><span>Men’s haircut</span><span class="price">$25</span></div>
      <div class="service-row"><span>Kid’s haircut (8 &amp; Under)</span><span class="price">$12</span></div>
      <div class="service-row"><span>Kid’s haircut (8 to 16)</span><span class="price">$18</span></div>
      <div class="service-row"><span>Girls haircut &amp; blow dry</span><span class="price">$35</span></div>
      <div class="service-row"><span>Hair cut &amp; blow dry</span><span class="price">$50</span></div>
      <div class="service-row"><span>Roller set &amp; blow dray or</span><span class="price">$55</span></div>
      <div class="service-note">flat iron</div>
      <div class="service-row"><span>Iron or curling with service</span><span class="price">$10</span></div>
    </div>
    <div class="service-group">
      <div class="group-title">Conditioning</div>
      <div class="service-row"><span>Hair recovery treatment</span><span class="price">$20</span></div>
      <div class="service-row"><span>Deep condition</span><span class="price">$15</span></div>
      <div class="service-row"><span>Keratin</span><span class="price">$300+</span></div>
      <div class="service-row"><span>Retouch</span><span class="price">$220</span></div>
    </div>
    <div class="service-group">
      <div class="group-title">Colors</div>
      <div class="service-row"><span>All over color</span><span class="price">$75</span></div>
      <div class="service-row"><span>Color touchup</span><span class="price">$55</span></div>
      <div class="service-row"><span>Full highlights</span><span class="price">$125+</span></div>
      <div class="service-row"><span>Partial highlights</span><span class="price">$75+</span></div>
      <div class="service-row"><span>Corrective Color</span><span class="price">$75+</span></div>
      <div class="service-row"><span>Updos</span><span class="price">$65+</span></div>
    </div>
    <div class="service-group">
      <div class="group-title">Perms</div>
      <div class="service-row"><span>Relaxer with haircut style</span><span class="price">$85</span></div>
      <div class="service-row"><span>Curly Perms</span><span class="price">$95</span></div>
    </div>
  </section>

  <div class="language-band">se habla español</div>
</div>
</body>
</html>
```